Awesome business card design needed

We need a new business card design to go with our new logo.
We are a web development agency that specialises in highly complex back-end integrations as opposed to design, our customers are retailers, hotels, hospitals and any other organisation that has a large online marketing department.
Take a look at our website - www.orvekplus.com for some inspiration.
We want our new business cards to exude class, professionalism and style.
We are likely to choose a high-end card to print them on but we want the design of the card itself to really turn heads.
We have no specific colour requirements, the logo as you will see is a turquoise colour R89 G171 B167 #59aba7 but it can also be in white if you want to make the colour of the card something different.
The information on the card should be:
Name
Position
Tel
email
Potentially a double sided card could have our web address, twitter and FB links.

```html
<!DOCTYPE html>
<html lang="en">
<head>
<meta charset="utf-8">
<title>orvekplus business card</title>
<link rel="stylesheet" href="https://fonts.googleapis.com/css2?family=Lato:wght@400;700;900&family=Tinos&display=swap">
<style>
  :root {
    --page: #e9e9e7;
    --card-black: #1b1c1d;
    --card-charcoal: #2a2c2e;
    --teal: #59aba7;
    --teal-bright: #4fc2b0;
    --teal-deep: #0f6b59;
    --teal-mid: #1e9a80;
    --silver: #c9cdd0;
    --white: #ffffff;
  }
  * { margin: 0; padding: 0; box-sizing: border-box; }
  html, body { width: 1200px; height: 900px; overflow: hidden; background: var(--page); }
  .canvas {
    position: relative; width: 1200px; height: 900px;
    display: flex; flex-direction: column; align-items: center; justify-content: center; gap: 50px;
  }
  .card {
    position: relative; width: 600px; height: 343px; overflow: hidden;
    box-shadow: 0 6px 18px rgba(0,0,0,.18);
  }
  .card-front { background: linear-gradient(160deg, var(--card-charcoal), var(--card-black) 60%); }
  .front-swoosh { position: absolute; inset: 0; width: 100%; height: 100%; }
  .holder-name {
    position: absolute; left: 40px; top: 26px;
    font: 400 32px/1 "Lato", sans-serif; color: var(--teal-bright); letter-spacing: .5px;
  }
  .holder-position {
    position: absolute; left: 62px; top: 64px;
    font: 400 17px/1 "Tinos", serif; color: var(--white);
  }
  .wordmark {
    position: absolute; right: 34px; top: 88px;
    font: 900 50px/1 "Lato", sans-serif; color: var(--teal); letter-spacing: 1px;
  }
  .contact { position: absolute; left: 262px; top: 148px; list-style: none; }
  .contact li {
    display: flex; align-items: center; gap: 12px; margin-bottom: 12px;
    font: 400 17px/1 "Tinos", serif; color: var(--white);
  }
  .contact svg { width: 18px; height: 18px; flex: none; }
  .card-back { background: linear-gradient(135deg, #4ec3a6 0%, var(--teal-mid) 45%, var(--teal-deep) 100%); }
  .back-artwork {
    position: absolute; inset: 0;
    background: radial-gradient(circle at 40% 35%, #2f6f66 0%, #3aa48c 30%, rgba(79,194,166,0) 62%);
  }
  .back-wordmark {
    position: absolute; left: 50%; top: 50%; transform: translate(-50%, -50%);
    font: 900 72px/1 "Lato", sans-serif; color: var(--white); letter-spacing: 1px;
  }
</style>
</head>
<body>
<main class="canvas">
  <section class="card card-front" aria-label="Card front">
    <svg class="front-swoosh" viewBox="0 0 600 343" preserveAspectRatio="none" aria-hidden="true">
      <defs>
        <linearGradient id="tealBand" x1="0" y1="0" x2="0" y2="1">
          <stop offset="0" stop-color="#3fbfa2"/>
          <stop offset="1" stop-color="#0f7a63"/>
        </linearGradient>
      </defs>
      <path d="M0 150 C 170 160, 330 265, 600 320 L600 343 L0 343 Z" fill="url(#tealBand)"/>
      <path d="M0 150 C 170 160, 330 265, 600 320" fill="none" stroke="var(--silver)" stroke-width="7"/>
    </svg>
    <h1 class="holder-name">Your Name</h1>
    <p class="holder-position">Your Position</p>
    <p class="wordmark">orvekplus</p>
    <ul class="contact">
      <li>
        <svg viewBox="0 0 18 18"><rect width="18" height="18" rx="2" fill="var(--teal)"/><path d="M6 4c-2 2-2 6 2 10l1-2-2-2 1-2-1-3z" fill="var(--card-black)"/></svg>
        000000000
      </li>
      <li>
        <svg viewBox="0 0 18 18"><rect width="18" height="18" rx="2" fill="var(--teal)"/><rect x="3" y="5" width="12" height="8" fill="none" stroke="var(--card-black)" stroke-width="1.4"/><path d="M3 5l6 5 6-5" fill="none" stroke="var(--card-black)" stroke-width="1.4"/></svg>
        Youremail@orvekplus.com
      </li>
    </ul>
  </section>

  <section class="card card-back" aria-label="Card back">
    <div class="back-artwork" role="img" aria-label="Digital eye illustration with teal rings, hexagons and light streaks"></div>
    <p class="back-wordmark">orvekplus</p>
  </section>
</main>
</body>
</html>
```